Heritage Hollow Business Cards

Require a business card design. <br/><br/>Needs to include logo (either round or long version) plus these details:<br/>Maya Torvel<br/>Heritage Hollow<br/>maya@quonbrook.com.au<br/>02 6481 7390<br/>PO Box Glenwarra NSW 2913<br/>www.heritagehollow.com.au<br/><br/>I need in an editable format so that I can create for multiple staff members. <br/><br/>

Target Market(s)

We are an online store selling renovation products to home owners are builders. Looking for a classic classy design.

Industry/Entity Type

Home And Garden

Contact Information for Business Card

Maya Torvel
Heritage Hollow
maya@quonbrook.com.au
02 6481 7390
PO Box Glenwarra NSW 2913
www.heritagehollow.com.au

Colors

Designer to choose colors to be used in the design.

Requirements
Must have
• Must include Logo.

```html
<!DOCTYPE html>
<html lang="en">
<head>
<meta charset="utf-8">
<title>Heritage Hollow Business Cards</title>
<link href="https://fonts.googleapis.com/css2?family=Arimo:wght@400;700&display=swap" rel="stylesheet">
<style>
  :root {
    --orange: #e8561f;
    --ink: #1f1f1f;
    --pill: #3a3a3a;
    --paper: #ffffff;
    --grey-text: #555555;
    --backdrop: #d9dde3;
    --rule: #9a9a9a;
  }
  * { margin: 0; padding: 0; box-sizing: border-box; }
  html, body { width: 1200px; height: 675px; overflow: hidden; }
  body {
    background: var(--backdrop);
    font-family: "Arimo", Arial, sans-serif;
    position: relative;
  }
  .card {
    position: absolute;
    top: 187px;
    width: 525px;
    height: 300px;
    background: var(--paper);
    overflow: hidden;
    box-shadow: 0 6px 18px rgba(0,0,0,0.18);
  }
  .card--front { left: 50px; }
  .card--back { left: 625px; }

  /* front */
  .front__tab {
    position: absolute;
    width: 14px;
    height: 70px;
    background: var(--ink);
  }
  .front__tab--left { left: 0; top: 110px; }
  .front__tab--right { right: 0; top: 40px; }
  .brand {
    display: flex;
    align-items: center;
    gap: 10px;
  }
  .brand__mark {
    width: 26px;
    height: 26px;
    background: var(--orange);
  }
  .brand__name {
    font-weight: 700;
    color: var(--ink);
    white-space: nowrap;
  }
  .front__brand {
    position: absolute;
    left: 0; right: 0;
    top: 100px;
    justify-content: center;
  }
  .front__brand .brand__name { font-size: 36px; }
  .front__band {
    position: absolute;
    left: 0; right: 0; bottom: 0;
    height: 62px;
    background: var(--ink);
    display: flex;
    align-items: center;
    justify-content: center;
    color: var(--paper);
    font-size: 19px;
    letter-spacing: 3px;
  }

  /* back */
  .back__top { position: absolute; left: 0; right: 0; top: 0; height: 165px; }
  .back__brand { position: absolute; left: 40px; top: 72px; }
  .back__brand .brand__mark { width: 20px; height: 20px; }
  .back__brand .brand__name { font-size: 25px; }
  .back__divider {
    position: absolute;
    left: 285px; top: 30px;
    width: 1px; height: 105px;
    background: var(--rule);
  }
  .person {
    position: absolute;
    right: 40px; top: 48px;
    text-align: right;
  }
  .person__name {
    color: var(--orange);
    font-weight: 700;
    font-size: 20px;
    letter-spacing: 0.5px;
  }
  .person__role {
    color: var(--grey-text);
    font-size: 15px;
    margin-top: 2px;
  }
  .back__band {
    position: absolute;
    left: 0; right: 0; bottom: 0;
    height: 135px;
    background: var(--ink);
  }
  .icon-pill {
    position: absolute;
    left: 0;
    width: 68px;
    height: 38px;
    background: var(--pill);
    border-radius: 0 19px 19px 0;
    display: flex;
    align-items: center;
    justify-content: center;
  }
  .icon-pill--phone { top: 22px; }
  .icon-pill--web { top: 74px; }
  .contact__phone {
    position: absolute;
    left: 88px; top: 20px;
    color: var(--paper);
    font-weight: 700;
    font-size: 24px;
    letter-spacing: 2px;
  }
  .contact__lines {
    position: absolute;
    left: 88px; top: 72px;
    color: var(--paper);
    font-size: 15px;
    line-height: 20px;
  }
  .address {
    position: absolute;
    right: 30px; top: 22px;
    color: var(--orange);
    font-size: 15px;
    line-height: 20px;
    text-align: right;
  }
</style>
</head>
<body>

<section class="card card--front" aria-label="Business card front">
  <span class="front__tab front__tab--left"></span>
  <span class="front__tab front__tab--right"></span>
  <div class="brand front__brand">
    <span class="brand__mark"></span>
    <span class="brand__name">Heritage Hollow</span>
  </div>
  <div class="front__band">www.heritagehollow.com.au</div>
</section>

<section class="card card--back" aria-label="Business card back">
  <div class="back__top">
    <div class="brand back__brand">
      <span class="brand__mark"></span>
      <span class="brand__name">Heritage Hollow</span>
    </div>
    <span class="back__divider"></span>
    <div class="person">
      <div class="person__name">MAYA TORVEL</div>
      <div class="person__role">Director</div>
    </div>
  </div>
  <div class="back__band">
    <div class="icon-pill icon-pill--phone">
      <svg width="24" height="24" viewBox="0 0 24 24" fill="none" stroke="var(--orange)" stroke-width="2">
        <circle cx="12" cy="12" r="10"/>
        <path d="M8.5 7.5c-.8.8-.6 2.6 1.4 4.8s4 2.9 5 2.1l1-1-2-1.6-1 .8c-.8-.3-2.2-1.6-2.6-2.6l.8-1-1.6-2z" fill="var(--orange)" stroke="none"/>
      </svg>
    </div>
    <div class="icon-pill icon-pill--web">
      <svg width="24" height="24" viewBox="0 0 24 24" fill="none" stroke="var(--orange)" stroke-width="2">
        <circle cx="12" cy="12" r="10"/>
        <ellipse cx="12" cy="12" rx="4.5" ry="10"/>
        <line x1="2" y1="12" x2="22" y2="12"/>
        <line x1="3.5" y1="7" x2="20.5" y2="7"/>
        <line x1="3.5" y1="17" x2="20.5" y2="17"/>
      </svg>
    </div>
    <div class="contact__phone">02 6481 7390</div>
    <div class="contact__lines">
      <div>maya@quonbrook.com.au</div>
      <div>www.heritagehollow.com.au</div>
    </div>
    <div class="address">
      <div>PO Box Glenwarra</div>
      <div>NSW 2913</div>
    </div>
  </div>
</section>

</body>
</html>
```